Photography Company Seeks Amazing and Fun Website Design

Note: This is for design only. No coding required. We want to see your ideas for a great website! This will be a FUN design and not boring like others you may work on.

Please let your creative ideas flow. We have given you a ton of info along with videos to help you understand what we are after, however we WANT your creativity to shine through in your designs!

We are a professional company that has run hundreds of crowdsourced projects on multiple platforms. If you participate in this contest (we hope you do) you can expect great video feedback, consistent feedback, and also our guarantee that if we know your website design will not be what we are looking for we will notify you so you don’t waste your time if there is no chance of you winning.

We respect and recognize this is how you make your living and we will not play games. We look forward to an awesome contest and awesome website designs.

Design Brief:

We are looking for a stunning website design to showcase this amazing photography company. Their current site is:

http://www.tervaloshots.example/

As you can see they do amazing photography and need an amazing website to showcase their work and to attract new people into their studios.

We are looking to get a website that is clean, classy, bright, artistic, and that really helps this company stand out amongst other photography companies.

We need a homepage and an interior page mockup.

Here are some examples of other sites in their business with what we like:

http://www.brakovenstudio.example/

Please watch video to learn what we like and don’t like:http://clipvault.example/t/QZpLm4wXr2d

http://www.harbinglenswork.example/

Please watch video to learn what we like and don’t like: http://clipvault.example/t/Wb7gkR2nvsQj

NOTE: We do not want to copy anything outright. We want to learn, model and take their ideas and make them better. We also want to be flexible and take what we like along with your creativity to make an amazing design.

Here is what we are looking for in more specific terms:

NOTE: Website should have a spot for video on the homepage.

This website is for a very professional and well know photography company. Because it is photography the website needs to be VERY visual.

Site should be unique and really stand out to help sell the business and their services. EVERYTHING about this business is visual, so the site MUST reflect that.

Site Overall: Fun and Artistic. This is a forward thinking company that is fun, upbeat, and does things differently, they need the design to reflect that. This is a modern photography company.

They also do all kinds of photography from school kids, sports teams, in studio shoots with High School Seniors, Family Pictures etc.

Colors: We like the white background because it is clean and really helps the photos stand out. Also please look at the logo too. Use colors from that and make things flow. Again we want this to stand out and be different while at the same time being clean.

Menu: Horizontal. We like bold and easy to read menu items. Don’t make it small and cluttered. Include the same items that are in the other site for the mock up.

Site Structure: Clean and easy to navigate. We have a lot of content to display so we need a clean structure that breaks up the text and content areas.

Images: Please pull images from the current site. We can always replace the images of course, but if you show them “their own stuff” in the new design you will be closer to winning because it will feel more like “them”

Content Areas: It is a safe bet that if it is on the current site we need it on the new site. So don’t drop anything as it makes it hard to “cut content”.

What we don't want: We do not want clutter, boring, or templates or themes. We don’t want too cartoony, too cute, or too fancy. We don’t want ugly.

Out of respect to professional designers who really are working hard to win if you do not follow this brief, you submit worn out themes, templates, or boring designs you will be eliminated. We are offering great prize money for this so we expect great visual designs.

Thanks,

The Quillstone Team

Target Market(s)

Target Market are upper middle class who want a better photography studio then the average studio, but don't want to go to the highest end of photography. This studio will cater to higher middle class.

Industry/Entity Type

Business

Number of Pages Required

1 page

Font styles to use
Sans Serif

Requirements
Must have
• Video on Home page
• Clean
• Stand Out
• Fun
• Professional
Nice to have
• Creative
• Lots of content in a great structure
Should not have
• clutter
• ugly design
• messy

```html
<!DOCTYPE html>
<html lang="en">
<head>
<meta charset="utf-8">
<title>Tervalo Photography</title>
<link href="https://fonts.googleapis.com/css2?family=Fredoka:wght@300;400;500;600&family=Open+Sans:wght@400;600;700&display=swap" rel="stylesheet">
<style>
:root{
  --purple:#9a3a88;
  --magenta:#a4358f;
  --red:#d3122c;
  --green:#2e8b4c;
  --orange:#f47a38;
  --blue:#2d8ccc;
  --cta:#e6502a;
  --submit:#136f9b;
  --ink:#2a2a2a;
  --muted:#555;
  --footer:#1b1b1d;
  --footer-bar:#0b0b0c;
  --white:#fff;
}
*{margin:0;padding:0;box-sizing:border-box}
html,body{width:1200px;height:2862px;overflow:hidden}
body{position:relative;background:var(--white);font-family:"Open Sans",Arial,sans-serif;color:var(--ink)}
h1,h2,h3,h4{font-weight:400}
.abs{position:absolute}

/* header */
.brand{left:100px;top:36px;display:flex;align-items:center;gap:12px}
.brand-dot{width:34px;height:34px;border-radius:50%;background:var(--purple)}
.brand-name{font-family:"Fredoka",sans-serif;font-weight:500;font-size:44px;color:var(--ink)}
.main-nav{right:56px;top:40px;display:flex;gap:38px;font-family:"Fredoka",sans-serif;font-size:17px;font-weight:400;color:var(--ink)}

/* hero */
.hero-title{left:97px;top:318px;font-family:"Fredoka",sans-serif;font-weight:600;font-size:62px;line-height:62px;color:var(--white)}
.btn-booking{left:99px;top:476px;width:150px;height:43px;background:var(--magenta);color:var(--white);font-family:"Fredoka",sans-serif;font-size:17px;display:flex;align-items:center;justify-content:center}
.hero-arrow{top:412px}

/* welcome */
.video{left:99px;top:832px;width:403px;height:288px;background:#000;box-shadow:0 2px 6px rgba(0,0,0,.3)}
.video-play{position:absolute;left:167px;top:90px;width:72px;height:72px;border-radius:50%;background:rgba(255,255,255,.35)}
.video-bar{position:absolute;left:0;bottom:0;width:100%;height:30px;background:#f1f1f1;display:flex;align-items:center;padding:0 10px;gap:14px;font-size:8px;color:#333}
.track{position:relative;width:200px;height:3px;background:#333}
.track i{position:absolute;left:0;top:0;width:95px;height:3px;background:var(--red)}
.welcome-title{left:600px;top:820px;width:492px;text-align:center;font-family:"Fredoka",sans-serif;font-size:40px;font-weight:400}
.welcome-title span{color:var(--magenta)}
.welcome-rule{left:676px;top:902px;width:400px;border-top:1px dotted #bbb}
.welcome-cam{left:827px;top:892px}
.welcome-copy{left:605px;top:940px;width:490px;text-align:center;font-size:11px;line-height:20px;color:var(--muted)}
.welcome-copy p{margin-bottom:18px}
.btn-read{left:801px;top:1097px;width:99px;height:33px;background:var(--cta);color:var(--white);font-size:11px;display:flex;align-items:center;justify-content:center}

/* studio */
.studio-title{right:97px;top:1224px;font-family:"Fredoka",sans-serif;font-size:42px;font-weight:400;color:var(--white)}
.card{top:1301px;width:231px;height:346px;background:var(--white)}
.card-head{height:50px;color:var(--white);font-family:"Fredoka",sans-serif;font-size:17px;display:flex;align-items:center;justify-content:center}
.card-img{display:block;width:231px;height:150px}
.card-text{padding:16px 12px 0;text-align:center;font-size:11px;line-height:20px;color:var(--muted)}
.card-btn{margin:16px auto 0;width:100px;height:30px;background:#222;color:var(--white);font-size:10px;display:flex;align-items:center;justify-content:center}

/* blog */
.blog-title{left:0;top:1742px;width:1200px;text-align:center;font-family:"Fredoka",sans-serif;font-weight:500;font-size:32px;color:var(--magenta)}
.post{top:1818px;width:311px;text-align:center}
.post h3{font-family:"Fredoka",sans-serif;font-weight:400;font-size:17px;margin-bottom:18px}
.post-img{display:block;width:311px;height:191px}
.post-date{margin-top:12px;font-family:"Fredoka",sans-serif;font-size:15px;color:#1f5a7a}
.post p{margin-top:6px;padding:0 22px;font-size:12px;line-height:22px;color:var(--muted)}

/* newsletter */
.notify{left:97px;top:2276px;display:flex;align-items:center;gap:24px}
.notify-title{font-family:"Fredoka",sans-serif;font-weight:500;font-size:30px;line-height:36px;color:var(--white);text-align:center}
.subscribe-note{left:478px;top:2270px;font-size:18px;color:var(--white)}
.subscribe{left:473px;top:2316px;width:626px;height:50px;display:flex;border-radius:25px;overflow:hidden}
.subscribe-input{flex:1;background:var(--white);color:#aaa;font-size:15px;padding-left:22px;display:flex;align-items:center}
.subscribe-btn{width:150px;background:var(--submit);color:var(--white);font-weight:700;font-size:18px;display:flex;align-items:center;justify-content:center}

/* footer */
.foot-col h4{font-family:"Fredoka",sans-serif;font-weight:500;font-size:17px;color:var(--white);margin-bottom:14px}
.foot-list{list-style:none;font-size:11px;line-height:27px;color:#b8b8b8}
.foot-list li::before{content:"›";margin-right:10px;color:#999}
.contact{font-size:13px;color:#e6e6e6;line-height:22px}
.contact-row{display:flex;align-items:center;gap:14px;margin-top:14px}
.socials{display:flex;gap:22px;margin-top:20px}
.socials span{width:32px;height:32px;border-radius:50%}
.sport{display:flex;gap:18px;margin-bottom:30px}
.sport-img{width:102px;height:74px}
.sport-text strong{display:block;font-weight:400;font-size:15px;color:#9a9a9a}
.sport-text small{display:block;font-size:10px;color:#777;line-height:14px;margin-top:4px}
.sport-text em{display:block;font-style:normal;font-size:10px;color:#9b86c4;margin-top:6px}
.copyright{left:0;top:2815px;width:1200px;text-align:center;font-size:12px;color:#ddd}
</style>
</head>
<body>

<!-- band shapes -->
<svg class="abs" style="left:0;top:0" width="1200" height="2862" aria-hidden="true">
  <defs>
    <linearGradient id="welcomeBg" x1="0" y1="0" x2="1" y2="1">
      <stop offset="0" stop-color="#f6f6f6"/><stop offset=".45" stop-color="#e4e2e1"/><stop offset="1" stop-color="#f7f7f7"/>
    </linearGradient>
    <radialGradient id="welcomeGlow" cx=".35" cy=".25" r=".35">
      <stop offset="0" stop-color="#cfcac6"/><stop offset="1" stop-color="#cfcac6" stop-opacity="0"/>
    </radialGradient>
    <linearGradient id="studioBg" x1="0" y1="0" x2="1" y2="0">
      <stop offset="0" stop-color="#8a3a7d"/><stop offset="1" stop-color="#9c3b8c"/>
    </linearGradient>
    <radialGradient id="studioShade" cx=".1" cy=".2" r=".3">
      <stop offset="0" stop-color="#6a2c60"/><stop offset="1" stop-color="#6a2c60" stop-opacity="0"/>
    </radialGradient>
  </defs>
  <rect x="0" y="760" width="1200" height="480" fill="url(#welcomeBg)"/>
  <rect x="0" y="760" width="1200" height="480" fill="url(#welcomeGlow)"/>
  <polygon points="0,1231 1200,1183 1200,1708 0,1689" fill="url(#studioBg)"/>
  <polygon points="0,1231 1200,1183 1200,1708 0,1689" fill="url(#studioShade)"/>
  <polygon points="0,2226 1200,2202 1200,2482 0,2390" fill="var(--purple)"/>
  <polygon points="0,2390 1200,2482 1200,2862 0,2862" fill="var(--footer)"/>
  <rect x="0" y="2786" width="1200" height="76" fill="var(--footer-bar)"/>
</svg>

<!-- hero photo -->
<svg class="abs" style="left:0;top:0" width="1200" height="790" role="img" aria-label="Photographer laughing while shooting with a large lens camera">
  <defs>
    <linearGradient id="heroFill" x1="0" y1="0" x2="1" y2="0">
      <stop offset="0" stop-color="#9a9795"/><stop offset=".3" stop-color="#b4b0ac"/><stop offset=".5" stop-color="#8c8580"/><stop offset=".75" stop-color="#a07e6a"/><stop offset="1" stop-color="#c9bfb6"/>
    </linearGradient>
    <radialGradient id="heroDark" cx=".5" cy=".42" r=".26">
      <stop offset="0" stop-color="#1a1a1c"/><stop offset=".6" stop-color="#2b2a2b" stop-opacity=".7"/><stop offset="1" stop-color="#2b2a2b" stop-opacity="0"/>
    </radialGradient>
    <radialGradient id="heroWarm" cx=".88" cy=".45" r=".25">
      <stop offset="0" stop-color="#d29a7a"/><stop offset="1" stop-color="#d29a7a" stop-opacity="0"/>
    </radialGradient>
    <radialGradient id="heroBlue" cx=".82" cy=".98" r=".22">
      <stop offset="0" stop-color="#7b93ad"/><stop offset="1" stop-color="#7b93ad" stop-opacity="0"/>
    </radialGradient>
  </defs>
  <polygon points="0,149 1200,86 1200,782 0,706" fill="url(#heroFill)"/>
  <polygon points="0,149 1200,86 1200,782 0,706" fill="url(#heroDark)"/>
  <polygon points="0,149 1200,86 1200,782 0,706" fill="url(#heroWarm)"/>
  <polygon points="0,149 1200,86 1200,782 0,706" fill="url(#heroBlue)"/>
  <polyline points="0,706 1200,782" stroke="var(--purple)" stroke-width="5" fill="none"/>
  <polyline points="268,135 500,123" stroke="var(--red)" stroke-width="5"/>
  <polyline points="500,123 720,111" stroke="var(--green)" stroke-width="5"/>
  <polyline points="720,111 960,99" stroke="var(--blue)" stroke-width="5"/>
  <polyline points="960,99 1200,86" stroke="var(--purple)" stroke-width="5"/>
  <polygon points="0,0 268,0 268,135 0,149" fill="var(--white)"/>
</svg>

<header>
  <div class="abs brand"><span class="brand-dot"></span><span class="brand-name">Tervalo</span></div>
  <nav class="abs main-nav"><span>Home</span><span>Studio</span><span>Super Senior Days</span><span>Book It!</span><span>Ordering</span><span>Sports</span><span>Contact</span></nav>
</header>

<section class="hero">
  <h1 class="abs hero-title">Amazing<br>Photography</h1>
  <div class="abs btn-booking">Booking Now</div>
  <svg class="abs hero-arrow" style="left:30px" width="26" height="48" aria-hidden="true"><polyline points="22,4 4,24 22,44" fill="none" stroke="#fff" stroke-width="3"/></svg>
  <svg class="abs hero-arrow" style="left:1142px" width="26" height="48" aria-hidden="true"><polyline points="4,4 22,24 4,44" fill="none" stroke="#fff" stroke-width="3"/></svg>
</section>

<section class="welcome">
  <div class="abs video">
    <div class="video-play"><svg width="72" height="72" aria-hidden="true"><polygon points="28,20 54,36 28,52" fill="#fff"/></svg></div>
    <div class="video-bar">
      <svg width="8" height="9" aria-hidden="true"><polygon points="0,0 8,4.5 0,9" fill="#222"/></svg>
      <span>10:00/00:03</span>
      <div class="track"><i></i></div>
      <svg width="12" height="10" aria-hidden="true"><polygon points="0,3 4,3 8,0 8,10 4,7 0,7" fill="#222"/></svg>
      <div class="track" style="width:40px"><i style="width:30px"></i></div>
    </div>
  </div>
  <h2 class="abs welcome-title">Welcome To <span>Tervalo</span></h2>
  <div class="abs welcome-rule"></div>
  <svg class="abs welcome-cam" width="38" height="20" aria-hidden="true"><rect x="0" y="0" width="38" height="20" fill="#f0efee"/><rect x="10" y="5" width="18" height="13" rx="2" fill="#333"/><rect x="15" y="2" width="8" height="4" fill="#333"/><circle cx="19" cy="11.5" r="4" fill="#fff"/><circle cx="19" cy="11.5" r="2" fill="#333"/></svg>
  <div class="abs welcome-copy">
    <p>Lorem ipsum dolor sit amet conse ctetur adipisicing elit, sed do eiusmod tempor incididunt ut labore et dolore magna aliqua. Ut enim ad minim veniam, quis nostrud exercitation ullamco laboris nisi ut aliquip ex ea commodo consequat. Duis aute irure.</p>
    <p>Lorem ipsum dolor sit amet conse ctetur adipisicing elit, sed do eiusmod tempor incididunt ut labore et dolore magna aliqua. Ut enim ad minim veniam, quis nostrud exercitation ullamco laboris nisi ut aliquip ex ea commodo consequat. Duis aute irure.</p>
  </div>
  <div class="abs btn-read">READ MORE</div>
</section>

<section class="studio">
  <h2 class="abs studio-title">Our Studio</h2>
  <article class="abs card" style="left:99px">
    <div class="card-head" style="background:var(--red)">Sitting Fees</div>
    <svg class="card-img" role="img" aria-label="Vintage camera on a table"><defs><linearGradient id="c1" x1="0" y1="0" x2="0" y2="1"><stop offset="0" stop-color="#7fa3b8"/><stop offset=".55" stop-color="#51606a"/><stop offset="1" stop-color="#3a2a22"/></linearGradient><radialGradient id="c1b" cx=".4" cy=".6" r=".35"><stop offset="0" stop-color="#1c1b1b"/><stop offset="1" stop-color="#1c1b1b" stop-opacity="0"/></radialGradient></defs><rect width="231" height="150" fill="url(#c1)"/><rect width="231" height="150" fill="url(#c1b)"/></svg>
    <p class="card-text">Lorem ipsum dolor sit amet, consectur adipiscing elit. Sed blandit massa vel mauris sollicitudin dignissim.</p>
    <div class="card-btn">READ MORE +</div>
  </article>
  <article class="abs card" style="left:355px">
    <div class="card-head" style="background:var(--green)">Specials</div>
    <svg class="card-img" role="img" aria-label="Camera surrounded by floating photo prints"><defs><linearGradient id="c2" x1="0" y1="0" x2="1" y2="1"><stop offset="0" stop-color="#4a3834"/><stop offset="1" stop-color="#0e0e10"/></linearGradient><radialGradient id="c2b" cx=".3" cy=".35" r=".4"><stop offset="0" stop-color="#9a6a5a"/><stop offset="1" stop-color="#9a6a5a" stop-opacity="0"/></radialGradient></defs><rect width="231" height="150" fill="url(#c2)"/><rect width="231" height="150" fill="url(#c2b)"/></svg>
    <p class="card-text">Lorem ipsum dolor sit amet, consectur adipiscing elit. Sed blandit massa vel mauris sollicitudin dignissim.</p>
    <div class="card-btn">READ MORE +</div>
  </article>
  <article class="abs card" style="left:612px">
    <div class="card-head" style="background:var(--orange)">Family Pricing Guide</div>
    <svg class="card-img" role="img" aria-label="Family playing in autumn leaves"><defs><linearGradient id="c3" x1="0" y1="0" x2="0" y2="1"><stop offset="0" stop-color="#f2c46a"/><stop offset=".5" stop-color="#dc8a34"/><stop offset="1" stop-color="#9c4718"/></linearGradient><radialGradient id="c3b" cx=".5" cy=".5" r=".3"><stop offset="0" stop-color="#f6e0b8"/><stop offset="1" stop-color="#f6e0b8" stop-opacity="0"/></radialGradient></defs><rect width="231" height="150" fill="url(#c3)"/><rect width="231" height="150" fill="url(#c3b)"/></svg>
    <p class="card-text">Lorem ipsum dolor sit amet, consectur adipiscing elit. Sed blandit massa vel mauris sollicitudin dignissim.</p>
    <div class="card-btn">READ MORE +</div>
  </article>
  <article class="abs card" style="left:868px">
    <div class="card-head" style="background:var(--blue)">Senior Pricing Guide</div>
    <svg class="card-img" role="img" aria-label="Senior sitting on rocks with a camera"><defs><linearGradient id="c4" x1="0" y1="0" x2="0" y2="1"><stop offset="0" stop-color="#d8d2c6"/><stop offset=".5" stop-color="#a8906e"/><stop offset="1" stop-color="#6e4e32"/></linearGradient><radialGradient id="c4b" cx=".45" cy=".3" r=".3"><stop offset="0" stop-color="#4d6482"/><stop offset="1" stop-color="#4d6482" stop-opacity="0"/></radialGradient></defs><rect width="231" height="150" fill="url(#c4)"/><rect width="231" height="150" fill="url(#c4b)"/></svg>
    <p class="card-text">Lorem ipsum dolor sit amet, consectur adipiscing elit. Sed blandit massa vel mauris sollicitudin dignissim.</p>
    <div class="card-btn">READ MORE +</div>
  </article>
</section>

<section class="blog">
  <h2 class="abs blog-title">OUE BLOG</h2>
  <article class="abs post" style="left:99px">
    <h3>Praesent Commodo Cursus Magna</h3>
    <svg class="post-img" role="img" aria-label="Child on a parent's shoulders in a green park"><defs><linearGradient id="b1" x1="0" y1="0" x2="0" y2="1"><stop offset="0" stop-color="#d2e68a"/><stop offset=".5" stop-color="#7fae3e"/><stop offset="1" stop-color="#36661f"/></linearGradient><radialGradient id="b1b" cx=".75" cy=".6" r=".3"><stop offset="0" stop-color="#8e2a2a"/><stop offset="1" stop-color="#8e2a2a" stop-opacity="0"/></radialGradient></defs><rect width="311" height="191" fill="url(#b1)"/><rect width="311" height="191" fill="url(#b1b)"/></svg>
    <div class="post-date">17 - FEB - 2015</div>
    <p>Lorem ipsum dolor sit amet, consectetur adipiscing elit. Sed blandit massa vel mauris sollicitudin dignissim.</p>
  </article>
  <article class="abs post" style="left:445px">
    <h3>Praesent Commodo Cursus Magna</h3>
    <svg class="post-img" role="img" aria-label="Young boy in a hat and coat"><defs><linearGradient id="b2" x1="0" y1="0" x2="1" y2="1"><stop offset="0" stop-color="#8a6a52"/><stop offset="1" stop-color="#241c18"/></linearGradient><radialGradient id="b2b" cx=".5" cy=".55" r=".3"><stop offset="0" stop-color="#8f8a82"/><stop offset="1" stop-color="#8f8a82" stop-opacity="0"/></radialGradient></defs><rect width="311" height="191" fill="url(#b2)"/><rect width="311" height="191" fill="url(#b2b)"/></svg>
    <div class="post-date">17 - FEB - 2015</div>
    <p>Lorem ipsum dolor sit amet, consectetur adipiscing elit. Sed blandit massa vel mauris sollicitudin dignissim.</p>
  </article>
  <article class="abs post" style="left:790px">
    <h3>Praesent Commodo Cursus Magna</h3>
    <svg class="post-img" role="img" aria-label="Volleyball players at the net in a gym"><defs><linearGradient id="b3" x1="0" y1="0" x2="0" y2="1"><stop offset="0" stop-color="#f1eeea"/><stop offset=".6" stop-color="#ddc7b2"/><stop offset="1" stop-color="#c07c4c"/></linearGradient><radialGradient id="b3b" cx=".35" cy=".55" r=".2"><stop offset="0" stop-color="#c93a3a"/><stop offset="1" stop-color="#c93a3a" stop-opacity="0"/></radialGradient><radialGradient id="b3c" cx=".7" cy=".45" r=".2"><stop offset="0" stop-color="#4a6ea8"/><stop offset="1" stop-color="#4a6ea8" stop-opacity="0"/></radialGradient></defs><rect width="311" height="191" fill="url(#b3)"/><rect width="311" height="191" fill="url(#b3b)"/><rect width="311" height="191" fill="url(#b3c)"/></svg>
    <div class="post-date">17 - FEB - 2015</div>
    <p>Lorem ipsum dolor sit amet, consectetur adipiscing elit. Sed blandit massa vel mauris sollicitudin dignissim.</p>
  </article>
</section>

<section class="newsletter">
  <div class="abs notify">
    <svg width="46" height="42" aria-hidden="true"><polygon points="2,20 44,2 32,40 22,26" fill="#fff"/><polyline points="22,26 44,2" stroke="var(--purple)" stroke-width="2"/></svg>
    <div class="notify-title">GET NOTIFIED OF<br>ANY UPDATES!</div>
  </div>
  <p class="abs subscribe-note">Subscribe to our newsletter to be notified about new version release</p>
  <div class="abs subscribe"><div class="subscribe-input">Your email address</div><div class="subscribe-btn">SUBMIT</div></div>
</section>

<footer>
  <div class="abs foot-col" style="left:99px;top:2508px">
    <h4>SUPER SENIOR DAYS</h4>
    <ul class="foot-list">
      <li>MARAVALE ACADEMY - TBD</li><li>MARAVALE HIGH - TBD</li><li>CEDAR BLUFF HERITAGE - TBD</li><li>RIDGEWAY - TBD</li><li>WESTBROOK - TBD</li><li>SIERRA VISTA - TBD</li>
    </ul>
  </div>
  <div class="abs foot-col" style="left:355px;top:2508px">
    <h4>NAVIGATION</h4>
    <ul class="foot-list">
      <li>Studio</li><li>Super Senior Days</li><li>Book It!</li><li>Ordering</li><li>Sports</li><li>Contact Us</li>
    </ul>
  </div>
  <div class="abs foot-col" style="left:538px;top:2508px">
    <h4>CONTACT US</h4>
    <p class="contact">Tervalo Photography, 418 Linden Crest<br>Road, Maravale, NM</p>
    <div class="contact-row contact"><svg width="16" height="16" aria-hidden="true"><path d="M3 1 L6 1 L7 5 L5 6 Q7 10 10 11 L11 9 L15 10 L15 13 Q15 15 13 15 Q2 14 1 3 Q1 1 3 1Z" fill="none" stroke="#ddd" stroke-width="1.3"/></svg><span style="font-size:16px">(555)013-7720</span></div>
    <div class="contact-row contact" style="margin-top:6px"><svg width="16" height="12" aria-hidden="true"><rect x="1" y="1" width="14" height="10" fill="none" stroke="#ddd" stroke-width="1.3"/><polyline points="1,1 8,7 15,1" fill="none" stroke="#ddd" stroke-width="1.3"/></svg><span style="font-size:12px">schools@tervaloshots.example</span></div>
    <div class="socials"><span style="background:#2a6fc9"></span><span style="background:#d8102a"></span><span style="background:var(--purple)"></span></div>
  </div>
  <div class="abs foot-col" style="left:801px;top:2492px">
    <h4>SPORTS</h4>
    <div class="sport">
      <svg class="sport-img" role="img" aria-label="Kids playing soccer on a field"><defs><linearGradient id="s1" x1="0" y1="0" x2="0" y2="1"><stop offset="0" stop-color="#cfe6f4"/><stop offset=".5" stop-color="#9cc47a"/><stop offset="1" stop-color="#4f8a2e"/></linearGradient></defs><rect width="102" height="74" fill="url(#s1)"/></svg>
      <div class="sport-text"><strong>Sed ut perspiciatis unde</strong><small>Lorem ipsum dolor sit amet, adip-<br>iscing elit, sed do eiusmod</small><em>25 APRIL. 2014</em></div>
    </div>
    <div class="sport">
      <svg class="sport-img" role="img" aria-label="Children in team uniforms outdoors"><defs><linearGradient id="s2" x1="0" y1="0" x2="0" y2="1"><stop offset="0" stop-color="#e3edf6"/><stop offset=".5" stop-color="#d7b49c"/><stop offset="1" stop-color="#b0704e"/></linearGradient></defs><rect width="102" height="74" fill="url(#s2)"/></svg>
      <div class="sport-text"><strong>Sed ut perspiciatis unde</strong><small>Lorem ipsum dolor sit amet, adip-<br>iscing elit, sed do eiusmod</small><em>25 APRIL. 2014</em></div>
    </div>
  </div>
  <p class="abs copyright">Copyright © 2015 Tervalo Photography . All Rights Reserved.</p>
</footer>

</body>
</html>
```